Startup that helps high growth companies expand to new office locations needs a polished website

Hello! We are a B2B startup helping fast growing companies expand to new office locations. We are in need of a polished, vibrant website that is modern and professional. Our mission is to accelerate tech-enabled economic opportunity beyond silicon valley.
- Our current site is: https://www.pellanworks.co
- We help companies in 3 steps: Discover, Expand, Align
- Discover = analysis on where a company should expand to
geographically
- Expand = manage the entire office build out process
- Align = ongoing support at the new office and help culturally aligning
new office to HQ
- Look through our deck which is attached in this brief and incorporate parts of our deck into the website, especially content and messaging! Slide 2 in particular is important, so I've taken a screenshot of it individually and attached it.
- Please also carefully read through our branding document which includes color palettes and examples of websites we like. However, we are open to any ideas you think are better in terms of color and font! https://slides.marnotech.io/deck/7Qz_K2pLwRt9XyVbN4cHsJ8dFmA3eUoGi5/view#page=n8k2m4q7_0_0
- We need a strong call to action for customers to contact us

We are also looking for a new logo! This logo should convey that we help companies expand beyond their current office locations.

Thanks! Looking forward to seeing your designs!

Target Market(s)

hypergrowth startups of 100-500 people

Logo Text

PellanWorks

Coding

Coded - Design and coding required

Number of Pages Required

2 page

Font styles to use
Sans Serif

Requirements
Must have
• - Clear call to action on landing page
• - A separate about us page. Please refer to the wireframe attached
• - Incorporate content from the current homepage at https://www.pellanworks.co/ (Discover, Expand, Align content, which are the 3 pieces of our offering)
• - Incorporate messaging in Slide 2 of attached company ppt. I've also taken a screenshot of it individually and attached it.
• - Testimonials sections on homepage
Nice to have
• - Incorporate other elements of the slide deck as you see fit

```html
<!DOCTYPE html>
<html lang="en">
<head>
<meta charset="utf-8">
<title>PellanWorks — Expansion Ops Concierge</title>
<link href="https://fonts.googleapis.com/css2?family=Mulish:wght@300;400;600;700;800&family=Montserrat:wght@500;600&display=swap" rel="stylesheet">
<style>
  :root {
    --teal: #1ea5a6;
    --ink: #1b1b1b;
    --text: #6b6b6b;
    --muted: #a5a5a5;
    --line: #e6e6e6;
    --band: #f1f1f1;
    --white: #ffffff;
  }
  * { margin: 0; padding: 0; box-sizing: border-box; }
  html, body { width: 1200px; height: 4252px; overflow: hidden; }
  body { position: relative; background: var(--white); font-family: "Mulish", sans-serif; color: var(--text); }
  .abs { position: absolute; }

  /* header */
  .brand { left: 40px; top: 18px; font-weight: 700; font-size: 19px; color: var(--ink); }
  .header-phone { left: 660px; top: 24px; font-size: 11px; color: var(--muted); }
  .header-phone b { color: var(--ink); font-weight: 700; font-size: 12px; }
  .header-social { left: 850px; top: 22px; display: flex; gap: 16px; padding-left: 18px; border-left: 1px solid var(--line); }
  .dot { width: 11px; height: 11px; border-radius: 50%; background: #7b7b7b; }
  .dot.teal { background: var(--teal); }
  .menu { left: 1108px; top: 22px; display: flex; align-items: center; gap: 10px; font-size: 11px; font-weight: 700; color: var(--ink); }
  .menu span.bars { width: 14px; height: 9px; border-top: 2px solid var(--ink); border-bottom: 2px solid var(--ink); position: relative; }
  .menu span.bars::after { content: ""; position: absolute; left: 0; right: 0; top: 1.5px; border-top: 2px solid var(--ink); }

  /* hero */
  .hero { left: 40px; top: 62px; width: 1122px; height: 576px;
    background: linear-gradient(180deg, #c9a178 0%, #d78a3f 30%, #8a6a52 58%, #3e4148 100%); }
  .hero-frame { left: 255px; top: 147px; width: 258px; height: 443px; border: 7px solid var(--teal); }
  .hero-title { left: 318px; top: 245px; font-family: "Montserrat", sans-serif; font-weight: 500; font-size: 44px; line-height: 62px; letter-spacing: 9px; color: var(--white); text-transform: uppercase; }
  .slider-dots { left: 900px; top: 522px; display: flex; gap: 8px; }
  .slider-dots i { width: 24px; height: 3px; background: rgba(255,255,255,.6); }
  .slider-dots i:first-child { background: var(--white); }

  /* about */
  .eyebrow { font-size: 10px; font-weight: 700; letter-spacing: 1.5px; color: var(--teal); text-transform: uppercase; }
  .about-eyebrow { left: 235px; top: 752px; }
  .about-title { left: 235px; top: 776px; width: 300px; font-size: 22px; line-height: 27px; font-weight: 700; color: var(--ink); }
  .about-copy { left: 235px; top: 908px; width: 300px; font-size: 10px; line-height: 17px; color: var(--muted); }
  .statement { left: 235px; top: 1062px; width: 280px; padding-left: 18px; border-left: 3px solid var(--teal); font-size: 14px; line-height: 20px; color: var(--ink); }
  .about-photo { left: 672px; top: 746px; width: 292px; height: 411px; background: linear-gradient(160deg, #bcd8ec 0%, #5f8db4 45%, #2c4058 80%, #a27a52 100%); }
  .about-rule { left: 760px; top: 1157px; width: 144px; height: 62px; border-bottom: 1px solid var(--line); }

  /* services */
  .service { top: 1386px; width: 264px; height: 358px; }
  .service-discover { left: 176px; background: linear-gradient(180deg, #5aaeb0 0%, #4f9ea8 60%, #3c6d87 100%); }
  .service-expand { left: 462px; background: linear-gradient(180deg, #4aa5aa 0%, #8f8a6e 55%, #e67f34 75%, #2a2522 100%); }
  .service-align { left: 751px; background: linear-gradient(180deg, #3e9ea7 0%, #5bb1b3 55%, #c9d3d2 100%); }
  .service-label { position: absolute; left: 22px; bottom: 18px; color: var(--white); font-size: 40px; font-weight: 600; line-height: 38px; }
  .service-label span { display: block; font-size: 28px; font-weight: 400; }

  /* testimonials */
  .testimonials { left: 37px; top: 1888px; width: 1125px; height: 530px; background: var(--band); }
  .section-title { left: 235px; top: 1985px; font-size: 22px; font-weight: 700; color: var(--ink); }
  .arrows { left: 928px; top: 1985px; display: flex; gap: 18px; font-size: 18px; color: #bbb; }
  .arrows b { color: var(--ink); font-weight: 400; }
  .quote-card { top: 2088px; width: 357px; height: 156px; background: var(--white); }
  .quote-card.one { left: 235px; }
  .quote-card.two { left: 609px; }
  .avatar { position: absolute; left: 20px; top: -18px; width: 56px; height: 56px; border-radius: 50%; background: linear-gradient(180deg, #d9d9d9, #8c8c8c); border: 3px solid var(--white); }
  .quote-name { position: absolute; left: 22px; top: 52px; font-size: 11px; color: var(--ink); font-weight: 600; }
  .quote-name span { color: var(--muted); font-weight: 400; }
  .quote-mark { position: absolute; right: 22px; top: 14px; font-size: 34px; font-weight: 800; color: var(--teal); line-height: 1; }
  .quote-text { position: absolute; left: 22px; top: 78px; width: 300px; font-size: 9.5px; line-height: 15px; color: var(--muted); }

  /* team */
  .side-label { font-size: 10px; line-height: 15px; font-weight: 600; letter-spacing: 1px; color: var(--ink); text-transform: uppercase; padding-top: 8px; border-top: 3px solid var(--teal); width: 60px; }
  .team-label { left: 244px; top: 2512px; }
  .member { width: 168px; height: 168px; background: linear-gradient(180deg, #eeeeee 0%, #d8d4cf 55%, #7f9bb4 100%); }
  .divider { left: 40px; top: 2912px; width: 1122px; height: 1px; background: var(--line); }

  /* map */
  .map { left: 40px; top: 2985px; width: 1122px; height: 408px; background: linear-gradient(90deg, #9fd0f0 0%, #cfe6c4 18%, #e8ecd8 50%, #cfe6c4 82%, #9fd0f0 100%); }

  /* contact */
  .touch-label { left: 238px; top: 3474px; }
  .city { left: 425px; top: 3472px; font-size: 24px; font-weight: 700; color: var(--ink); }
  .city span { color: #c9c9c9; font-weight: 400; }
  .small { font-size: 10px; line-height: 17px; color: var(--text); }
  .small b { color: var(--ink); font-weight: 700; }
  .addr { left: 425px; top: 3518px; }
  .mail { left: 425px; top: 3566px; }
  .call-label { left: 740px; top: 3478px; }
  .call-phone { left: 740px; top: 3500px; font-size: 26px; font-weight: 600; color: var(--ink); }
  .hours { left: 740px; top: 3552px; }
  .follow { left: 740px; top: 3630px; }
  .follow-dots { left: 740px; top: 3654px; display: flex; gap: 14px; }
  .follow-dots .dot { width: 10px; height: 10px; background: #9a9a9a; }
  .follow-dots .dot.teal { background: var(--teal); }

  .help-label { left: 238px; top: 3748px; }
  .field { height: 26px; border: 1px solid #e3e3e3; background: #fafafa; font-size: 9.5px; color: #b5b5b5; padding: 7px 10px; }
  .field.name { left: 425px; top: 3750px; width: 173px; }
  .field.email { left: 613px; top: 3750px; width: 170px; }
  .field.subject { left: 800px; top: 3750px; width: 173px; }
  .field.message { left: 425px; top: 3794px; width: 548px; height: 105px; }
  .send { left: 425px; top: 3934px; width: 108px; height: 32px; background: var(--teal); color: var(--white); font-size: 9px; font-weight: 700; letter-spacing: 1px; text-transform: uppercase; display: flex; align-items: center; justify-content: center; }

  /* footer */
  .footer-brand { left: 40px; top: 4112px; }
  .copyright { left: 215px; top: 4116px; font-size: 10px; line-height: 15px; color: var(--ink); }
  .footer-links { top: 4118px; font-size: 10px; line-height: 16px; color: var(--ink); list-style: none; }
  .footer-links .active { color: var(--teal); }
  .links-a { left: 468px; }
  .links-b { left: 720px; }
  .lang { left: 903px; top: 4118px; font-size: 10px; color: var(--ink); }
  .lang::after { content: " \2304"; color: var(--teal); }
  .footer-dots { left: 1012px; top: 4121px; display: flex; gap: 14px; }
  .footer-dots .dot { width: 10px; height: 10px; background: var(--ink); }
  .footer-dots .dot.teal { background: var(--teal); }
</style>
</head>
<body>

  <!-- header -->
  <div class="abs brand">PellanWorks</div>
  <div class="abs header-phone">Call us: <b>(212) 555 0148</b></div>
  <div class="abs header-social"><span class="dot teal"></span><span class="dot"></span><span class="dot"></span><span class="dot"></span><span class="dot"></span></div>
  <div class="abs menu">MENU <span class="bars"></span></div>

  <!-- hero -->
  <div class="abs hero" role="img" aria-label="City skyline of high-rise office towers at sunset"></div>
  <div class="abs hero-frame"></div>
  <h1 class="abs hero-title">PellanWorks<br>is your<br>turnkey<br>solution.</h1>
  <div class="abs slider-dots"><i></i><i></i><i></i></div>

  <!-- about -->
  <p class="abs eyebrow about-eyebrow">About us</p>
  <h2 class="abs about-title">We Are The Leaders In Expansion Ops Concierge for building effective distributed teams.</h2>
  <p class="abs about-copy">Our mission is to accelerate tech-enabled economic opportunity beyond silicon valley. For each project we establish relationships with partners who we know will help us create added value for your projects as well as bringing together the public and private sectors, we build sector-outstanding teams together knowledge as the team from each other.</p>
  <p class="abs statement">expansion-as-a-service takes the pain out of growing effective teams in new locations.</p>
  <div class="abs about-photo" role="img" aria-label="Glass office building against a blue sky"></div>
  <div class="abs about-rule"></div>

  <!-- services -->
  <div class="abs service service-discover" role="img" aria-label="Glass tower against a teal sky">
    <p class="service-label">Discover<span>&gt;</span></p>
  </div>
  <div class="abs service service-expand" role="img" aria-label="Skyscrapers at dusk with orange sunset glow">
    <p class="service-label">Expand<span>&gt;</span></p>
  </div>
  <div class="abs service service-align" role="img" aria-label="Tall office building viewed from below">
    <p class="service-label">Align<span>&gt;</span></p>
  </div>

  <!-- testimonials -->
  <div class="abs testimonials"></div>
  <h2 class="abs section-title">From Great Our Clients</h2>
  <div class="abs arrows"><span>&lsaquo;</span><b>&rsaquo;</b></div>
  <div class="abs quote-card one">
    <div class="avatar" role="img" aria-label="Client portrait"></div>
    <p class="quote-name">Owen Hartley <span>/ CEO of Northgate</span></p>
    <span class="quote-mark">&rdquo;</span>
    <p class="quote-text">They found our second city, built the office and kept the team aligned with HQ. Our expansion went faster than we planned and smoother than we hoped.</p>
  </div>
  <div class="abs quote-card two">
    <div class="avatar" role="img" aria-label="Client portrait"></div>
    <p class="quote-name">Mara Ellison <span>/ Head of People at Lumora</span></p>
    <span class="quote-mark">&rdquo;</span>
    <p class="quote-text">A true turnkey partner. From site analysis to opening day, every step was handled, and our new team feels like part of the company.</p>
  </div>

  <!-- team -->
  <p class="abs side-label team-label">Meet<br>our<br>team</p>
  <div class="abs member" style="left:428px;top:2512px" role="img" aria-label="Team member portrait"></div>
  <div class="abs member" style="left:618px;top:2512px" role="img" aria-label="Team member portrait"></div>
  <div class="abs member" style="left:805px;top:2512px" role="img" aria-label="Team member portrait"></div>
  <div class="abs member" style="left:428px;top:2702px" role="img" aria-label="Team member portrait"></div>
  <div class="abs member" style="left:618px;top:2702px" role="img" aria-label="Team member portrait"></div>
  <div class="abs divider"></div>

  <!-- map -->
  <div class="abs map" role="img" aria-label="Street map of Manhattan showing the office location"></div>

  <!-- contact -->
  <p class="abs side-label touch-label">Keep<br>in<br>touch</p>
  <h3 class="abs city">Manhattan, <span>New York</span></h3>
  <p class="abs small addr">500 Hudson St, 12th Floor Loft Building<br>Manhattan, New York</p>
  <p class="abs small mail"><b>Email:</b> hello@pellanworks.co<br><b>Skype:</b> pellanworks</p>
  <p class="abs small call-label">Call directly</p>
  <p class="abs call-phone">+(212) 555 0148</p>
  <p class="abs small hours"><b>Work Hours</b><br>Monday – Friday: 09:00 – 17:00<br>Saturday: 09:00 – 13:00, Sunday off</p>
  <p class="abs small follow"><b>Follow us</b></p>
  <div class="abs follow-dots"><span class="dot teal"></span><span class="dot"></span><span class="dot"></span><span class="dot"></span><span class="dot"></span></div>

  <p class="abs side-label help-label">You<br>need<br>help</p>
  <div class="abs field name">Insert your name</div>
  <div class="abs field email">Your email</div>
  <div class="abs field subject">Subject (optional)</div>
  <div class="abs field message">Here goes your message</div>
  <div class="abs send">Send message</div>

  <!-- footer -->
  <div class="abs brand footer-brand">PellanWorks</div>
  <p class="abs copyright">© PellanWorks<br>All Rights Reserved</p>
  <ul class="abs footer-links links-a"><li class="active">Site Map</li><li>Term &amp; Conditions</li><li>Privacy Policy</li><li>Help</li></ul>
  <ul class="abs footer-links links-b"><li>Our Location</li><li>Career</li><li>About</li><li>Contact</li></ul>
  <p class="abs lang">English</p>
  <div class="abs footer-dots"><span class="dot teal"></span><span class="dot"></span><span class="dot"></span><span class="dot"></span><span class="dot"></span></div>

</body>
</html>
```